Strategy and Technology Consulting - Our Story and Values Page

Interior Page design – Our History and Our Values

Our homepage has been designed and we are looking for a design for one of the interior pages. This interior page tells the story of Our History and Our Values

Because the homepage has been designed, we would like this interior page to reflect the design of the homepage without being a mirror image of the homepage.

This site will be implemented in WordPress using the Elementor framework.

Font: Poppins medium and Poppins dark
Illustrations: Our homepage illustrations were designed by “Welmo 1974” on Pixaborne. Compatible original or stock illustrations are welcome. Stock photography is also welcome. Welmo is also available through Welmo Trastek on Folivane

Uploaded Files
• Homepage design – this is the design we will use for our homepage. Contest entries should reflect this basic style but should be distinctly different from the homepage.
• Our History and Our Values – Wireframe – the basic layout of the page we are looking for.
• Our History and Our Values – Word document with the text supporting the wireframe.
• Color Palette – please use colors compatible with the palette attached.

Our Story - timeline
There is a timeline element in the wireframe. The wireframe displays this as a series of chevrons (arrows), but it does not need to be. Creativity in display of the timeline is appreciated.

Our Values
If you look at the Word document, you will see that there are a lot of words on the page. The winning design will present the information in a way that engages the user without overwhelming them with too much to read. For example, they may click on a value and see more information.

Target Market(s)

CIO's and Technology Executives

Number of Pages Required

1 page

Font styles to use
Sans Serif
Other font styles liked:
• Poppin

Requirements
Must have
• A timeline element, all of our values
Nice to have
• Clever timeline display

```html
<!DOCTYPE html>
<html lang="en">
<head>
<meta charset="utf-8">
<title>Our Story and Our Values</title>
<link href="https://fonts.googleapis.com/css2?family=Poppins:wght@400;500;600;700&display=swap" rel="stylesheet">
<style>
  :root{
    --navy:#1f5b8e;
    --navy-deep:#1d5289;
    --sky:#b9d9f0;
    --sky-soft:#a9cde9;
    --gold:#f2b417;
    --steel:#9fb4c4;
    --ink:#1c1c1c;
    --body:#4a4a4a;
    --line:#eceef2;
    --white:#ffffff;
  }
  *{margin:0;padding:0;box-sizing:border-box}
  html,body{width:1200px;height:3427px;overflow:hidden;background:var(--white)}
  body{font-family:'Poppins',sans-serif;position:relative;color:var(--body)}

  .section-title{position:absolute;left:0;width:1200px;text-align:center;font-weight:700;font-size:52px;letter-spacing:.5px}
  .story-title{top:112px;color:var(--navy)}

  /* timeline */
  .tl-bar{position:absolute;width:11px;height:64px;top:243px}
  .tl-vline{position:absolute;top:262px;height:334px;border-left:2px dotted var(--navy)}
  .tl-axis{position:absolute;top:595px;left:93px;width:1014px;border-top:2px dotted var(--navy)}
  .tl-node{position:absolute;top:584px;width:24px;height:24px;border-radius:50%;border:3px solid;background:var(--white)}
  .tl-node::after{content:"";position:absolute;left:50%;top:50%;width:6px;height:6px;margin:-3px 0 0 -3px;border-radius:50%}
  .tl-node.sky{border-color:var(--sky-soft)}
  .tl-node.sky::after{background:var(--sky-soft)}
  .tl-node.gold{border-color:var(--gold)}
  .tl-node.gold::after{background:var(--gold)}
  .tl-node.steel{border-color:var(--steel)}
  .tl-node.steel::after{background:var(--steel)}
  .tl-illustration{position:absolute;top:250px;width:92px;height:92px;border-radius:18px;background:linear-gradient(135deg,var(--sky) 0%,#7fb0d8 60%,var(--gold) 100%);opacity:.85}
  .tl-year{position:absolute;top:364px;width:260px;text-align:center;font-weight:600;font-size:31px;color:var(--navy)}
  .tl-list{position:absolute;top:420px;list-style:none;font-size:14.5px;line-height:20px;color:#555}
  .tl-list li{position:relative;padding-left:18px;margin-bottom:14px}
  .tl-list li::before{content:"";position:absolute;left:0;top:6px;width:10px;height:10px;border-radius:50%;background:var(--sky-soft)}
  .tl-list.gold li::before{background:var(--gold)}
  .tl-list .sub{list-style:none;margin-top:12px;padding-left:10px}
  .tl-list .sub li{padding-left:16px;margin-bottom:4px}
  .tl-list .sub li::before{content:"-";background:none;top:0;width:auto;height:auto;color:#555}
  .eureka{font-weight:600;color:var(--navy)}

  /* values band */
  .values-band{position:absolute;left:0;top:700px;width:1200px;height:509px}
  .values-title{top:1020px;color:var(--white)}

  /* value rows */
  .value-frame{position:absolute;height:290px;border:2px solid var(--line)}
  .value-frame.left{border-right:none;border-radius:145px 0 0 145px}
  .value-frame.right{border-left:none;border-radius:0 145px 145px 0}
  .value-photo{position:absolute;width:224px;height:224px;border-radius:50%}
  .value-text{position:absolute;width:556px}
  .value-text h3{font-weight:600;font-size:28px;color:var(--ink);margin-bottom:18px;letter-spacing:.2px}
  .value-text p{font-size:16px;line-height:21.5px;color:var(--body)}
</style>
</head>
<body>

<section class="story" aria-label="Our Story">
  <h1 class="section-title story-title">Our Story</h1>

  <div class="tl-bar" style="left:124px;background:var(--sky)"></div>
  <div class="tl-bar" style="left:447px;background:var(--gold)"></div>
  <div class="tl-bar" style="left:765px;background:var(--steel)"></div>
  <div class="tl-bar" style="left:1066px;background:var(--gold)"></div>

  <div class="tl-vline" style="left:129px"></div>
  <div class="tl-vline" style="left:452px"></div>
  <div class="tl-vline" style="left:770px"></div>
  <div class="tl-vline" style="left:1071px"></div>
  <div class="tl-axis"></div>

  <div class="tl-node sky" style="left:258px"></div>
  <div class="tl-node gold" style="left:596px"></div>
  <div class="tl-node steel" style="left:908px"></div>

  <div class="tl-illustration" role="img" aria-label="Illustration of a rising bar chart with a coin" style="left:226px"></div>
  <div class="tl-illustration" role="img" aria-label="Illustration of a light bulb inside a gear" style="left:565px"></div>
  <div class="tl-illustration" role="img" aria-label="Illustration of a leadership team at a table with a coin" style="left:884px"></div>

  <div class="tl-year" style="left:141px">2017 – 2019</div>
  <div class="tl-year" style="left:491px">2017 – 2019</div>
  <div class="tl-year" style="left:798px">2017 – 2019</div>

  <ul class="tl-list" style="left:153px;width:270px">
    <li>Growth Strategy Focus</li>
    <li>Consistent, Modest Growth</li>
    <li>Preliminary Focus on Technology</li>
    <li><span class="eureka">Eureka!</span>&nbsp; Implementing<br>strategy is hard.</li>
  </ul>
  <ul class="tl-list gold" style="left:504px;width:240px">
    <li>Pandemic Pauses Growth</li>
    <li>Rethinking :
      <ul class="sub">
        <li>the business model</li>
        <li>the delivery model</li>
      </ul>
    </li>
  </ul>
  <ul class="tl-list" style="left:811px;width:250px">
    <li>Leadership Team for Focus on<br>Essential Areas</li>
    <li>Rapid Growth</li>
    <li>Customer Success</li>
  </ul>
</section>

<section class="values-band" aria-hidden="true">
  <svg width="1200" height="509" viewBox="0 0 1200 509">
    <defs>
      <linearGradient id="bandFill" x1="0" y1="0" x2="0" y2="1">
        <stop offset="0" stop-color="#1d5289"/>
        <stop offset="1" stop-color="#5587b5"/>
      </linearGradient>
      <linearGradient id="streak" x1="0" y1="0" x2="1" y2="0">
        <stop offset="0" stop-color="#d8ebf8"/>
        <stop offset=".55" stop-color="#a9cde9"/>
        <stop offset="1" stop-color="#ffffff" stop-opacity="0"/>
      </linearGradient>
    </defs>
    <path d="M0 80 C180 0 380 20 560 70 C700 110 820 115 930 115 C760 120 640 105 520 80 C360 45 180 50 0 110 Z" fill="url(#streak)"/>
    <path d="M0 100 C200 20 420 60 600 100 C820 150 1000 150 1200 20 L1200 509 L0 509 Z" fill="url(#bandFill)"/>
    <path d="M0 130 C260 170 520 250 820 290 C1000 310 1120 260 1200 200 L1200 509 L0 509 Z" fill="#3a72a6" opacity=".55"/>
  </svg>
</section>
<h2 class="section-title values-title">Our Values</h2>

<section class="values" aria-label="Our Values">
  <div class="value-frame left" style="left:165px;top:1258px;width:750px"></div>
  <div class="value-photo" role="img" aria-label="Open hand holding a glowing network of connected people" style="left:203px;top:1291px;background:radial-gradient(circle at 55% 40%,#6fa4d6 0%,#1e4f86 45%,#0b2547 100%)"></div>
  <div class="value-text" style="left:456px;top:1318px">
    <h3>The Value of Every Human.&nbsp; Regardless</h3>
    <p>Each person's unique experiences and perspectives add vibrant hues to the tapestry of our shared existence.&nbsp; In a world where diversity paints the canvas of humanity, true beauty is found in recognizing the inherent and incalculable value of every human being.</p>
  </div>

  <div class="value-frame right" style="left:300px;top:1547px;width:755px"></div>
  <div class="value-photo" role="img" aria-label="Many hands stacked together in a circle of teamwork" style="left:795px;top:1574px;background:radial-gradient(circle at 50% 50%,#c99a78 0%,#7d8fa3 50%,#4d6e88 100%)"></div>
  <div class="value-text" style="left:209px;top:1616px">
    <h3>Collaboration</h3>
    <p>Collaboration&nbsp; Collaboration in work transforms individual endeavors into symphonies of collective achievement. Through collaboration, diverse talents converge, fostering a rich exchange of ideas that amplifies creativity, accelerates progress, and brings forth solutions beyond what a single mind could conceive.</p>
  </div>

  <div class="value-frame left" style="left:165px;top:1837px;width:750px"></div>
  <div class="value-photo" role="img" aria-label="Person with raised arms on a mountain summit at dusk" style="left:203px;top:1872px;background:linear-gradient(180deg,#3a6fa8 0%,#8fb0cc 45%,#d9b99a 62%,#4b4f55 75%,#2a2d33 100%)"></div>
  <div class="value-text" style="left:456px;top:1899px">
    <h3>Passion</h3>
    <p>Passion infuses our work with energy, transforming routine tasks into opportunities for creativity and innovation. Fueled by passion, individuals become unstoppable forces, driven to overcome challenges and achieve remarkable outcomes that benefit them and inspire those around them</p>
  </div>

  <div class="value-frame right" style="left:300px;top:2126px;width:755px"></div>
  <div class="value-photo" role="img" aria-label="Hand touching a glowing digital checkmark" style="left:795px;top:2153px;background:radial-gradient(circle at 50% 45%,#9cc6ea 0%,#2b5f93 35%,#0c2340 100%)"></div>
  <div class="value-text" style="left:209px;top:2195px">
    <h3>Excellence</h3>
    <p>Excellence isn't a destination; it's a continuous journey of refinement and growth. Striving for excellence cultivates a culture of continuous improvement, fostering innovation, credibility, and a lasting impact that resonates far beyond the immediate task.</p>
  </div>

  <div class="value-frame left" style="left:165px;top:2415px;width:750px"></div>
  <div class="value-photo" role="img" aria-label="Businessman ticking boxes on a checklist" style="left:203px;top:2448px;background:radial-gradient(circle at 40% 50%,#3a4d66 0%,#1b2a3f 60%,#0f1a29 100%)"></div>
  <div class="value-text" style="left:456px;top:2478px">
    <h3>Tenacity</h3>
    <p>Tenacity is the unwavering anchor that keeps us grounded amidst adversity, propelling us forward when faced with obstacles. The resilience to persist, adapt, and learn from setbacks leads to the mastery of skills and the fulfillment of ambitious goals.</p>
  </div>

  <div class="value-frame right" style="left:300px;top:2704px;width:755px"></div>
  <div class="value-photo" role="img" aria-label="Chalk drawing of a light bulb filled with gears" style="left:795px;top:2735px;background:radial-gradient(circle at 50% 45%,#5a5a5a 0%,#333 55%,#1e1e1e 100%)"></div>
  <div class="value-text" style="left:209px;top:2766px">
    <h3>Solution Mindset</h3>
    <p>A solution mindset is the compass that directs our focus from problems to possibilities. It empowers us to navigate challenges with a proactive mindset, igniting a journey of exploration and innovation that not only resolves issues but also paves the way for continuous growth and success.</p>
  </div>

  <div class="value-frame left" style="left:165px;top:2993px;width:750px"></div>
  <div class="value-photo" role="img" aria-label="Hands on a laptop with floating document and file icons" style="left:203px;top:3026px;background:radial-gradient(circle at 50% 60%,#c77a4a 0%,#4a5a6e 40%,#1c2533 100%)"></div>
  <div class="value-text" style="left:456px;top:3043px">
    <h3>Generosity</h3>
    <p>GenerosityGenerosity creates a virtuous cycle of goodwill, fostering a sense of unity and shared purpose among colleagues. By freely sharing knowledge, support, and resources, we uplift those around us and contribute to a collaborative environment where collective achievements flourish.</p>
  </div>
</section>

</body>
</html>
```